High School Hockey Player Banners

I have 22 players that i need cropped out and added to a background with the school logo, player names and player numbers. I have uploaded all players photos w/ names and number on each file name. i have uploaded the Stone Creek Hornets school logo as well as an example of something that i like to give you inspiration. The finish size is 24" tall and 18" wide

```html
<!DOCTYPE html>
<html lang="en">
<head>
<meta charset="utf-8">
<title>Player Banner – Matthew Kellenberg #05</title>
<link href="https://fonts.googleapis.com/css2?family=Anton&family=Black+Ops+One&display=swap" rel="stylesheet">
<style>
  :root {
    --page: #ffffff;
    --sky-deep: #1f74e0;
    --sky-bright: #2cc3f6;
    --sky-low: #3397ff;
    --crimson: #c41335;
    --brush-orange: #ff6a00;
    --brush-red: #d8242b;
    --ghost-blue: rgba(28, 88, 225, 0.55);
    --gold: #f2c21a;
    --white: #ffffff;
    --photo-light: #f2eeea;
    --photo-mid: #e0d6d0;
  }
  * { margin: 0; padding: 0; box-sizing: border-box; }
  html, body {
    width: 1200px; height: 1200px;
    overflow: hidden;
    background: var(--page);
  }
  .banner {
    position: absolute;
    left: 184px; top: 44px;
    width: 833px; height: 1111px;
    box-shadow: 0 3px 10px rgba(0,0,0,0.25);
    overflow: hidden;
  }
  .banner svg { display: block; width: 100%; height: 100%; }
  .jersey-number { font-family: "Anton", sans-serif; }
  .player-name { font-family: "Black Ops One", sans-serif; }
  .ghost-name { font-family: "Anton", sans-serif; }
  .team-name { font-family: "Anton", sans-serif; }
</style>
</head>
<body>
<main class="banner">
  <svg viewBox="0 0 833 1111" xmlns="http://www.w3.org/2000/svg">
    <defs>
      <linearGradient id="sky" x1="0" y1="0" x2="0" y2="1">
        <stop offset="0" stop-color="var(--sky-deep)"/>
        <stop offset="0.35" stop-color="var(--sky-bright)"/>
        <stop offset="0.6" stop-color="var(--sky-low)"/>
        <stop offset="1" stop-color="var(--sky-low)"/>
      </linearGradient>
      <linearGradient id="arena" x1="0" y1="0" x2="1" y2="1">
        <stop offset="0" stop-color="#1450b8" stop-opacity="0.85"/>
        <stop offset="0.6" stop-color="#1f74e0" stop-opacity="0.5"/>
        <stop offset="1" stop-color="#2cc3f6" stop-opacity="0"/>
      </linearGradient>
      <linearGradient id="brush" x1="0" y1="0" x2="0" y2="1">
        <stop offset="0" stop-color="var(--brush-orange)"/>
        <stop offset="1" stop-color="var(--brush-red)"/>
      </linearGradient>
      <linearGradient id="player" x1="0" y1="0" x2="0" y2="1">
        <stop offset="0" stop-color="var(--photo-light)"/>
        <stop offset="1" stop-color="var(--photo-mid)"/>
      </linearGradient>
    </defs>

    <rect class="backdrop" width="833" height="1111" fill="url(#sky)"/>

    <path class="arena-photo" role="img" aria-label="Tinted arena action photo of players celebrating along the boards"
          d="M0 0 H470 L440 150 L300 300 L0 380 Z" fill="url(#arena)"/>

    <text class="ghost-name" x="0" y="612" font-size="210" textLength="833" lengthAdjust="spacingAndGlyphs"
          fill="var(--ghost-blue)">MATTHEW</text>

    <path class="paint-brush"
          d="M175 620 L230 560 L330 520 L420 505 L470 480 L560 500 L640 470 L720 500 L833 470
             L833 800 L790 830 L740 870 L700 900 L640 930 L600 905 L540 936 L470 905
             L400 915 L340 880 L300 850 L250 830 L200 780 L180 700 Z"
          fill="url(#brush)"/>

    <text class="jersey-number" x="364" y="421" font-size="425" textLength="430" lengthAdjust="spacingAndGlyphs"
          fill="none" stroke="var(--white)" stroke-width="2">#05</text>
    <text class="jersey-number" x="358" y="418" font-size="425" textLength="430" lengthAdjust="spacingAndGlyphs"
          fill="var(--crimson)">#05</text>

    <rect class="player-photo" role="img" aria-label="Cut-out photo of the player skating in a white, red and gold jersey with helmet and stick"
          x="0" y="290" width="340" height="821" fill="url(#player)"/>

    <text class="player-name" x="356" y="663" font-size="70" textLength="334" lengthAdjust="spacingAndGlyphs"
          fill="var(--white)">MATTHEW</text>
    <text class="player-name" x="356" y="731" font-size="70" textLength="423" lengthAdjust="spacingAndGlyphs"
          fill="var(--white)">KELLENBERG</text>

    <text class="team-name" x="456" y="990" font-size="22" textLength="352" lengthAdjust="spacing"
          fill="var(--gold)">STONE CREEK</text>
    <text class="team-name" x="474" y="1055" font-size="66" textLength="314" lengthAdjust="spacing"
          fill="var(--crimson)">HORNETS</text>
  </svg>
</main>
</body>
</html>
```